Create Vertical Dog Food Labels (3 inches x 5 inches) for PupKitchen

We need a packing Vertical label (3 inches x 5 inches) design for our line of Dog Food - Pup Kitchen at pupkitchenmeals.com (please review website). This design is for Custom Roll Labels. We have a logo already. Use our logo colors on label. What we need incorporated is a list of our ingredients:

50% Choice Beef
20% Pasture-raised Chicken
15% Brown Rice
15% Fresh Vegetables - Carrots, Kale, Zucchini
Herbal Health Boosters

We also need these lines at the bottom of the label:

Keeps in fridge for 4 days after thawing
Stores in freezer up to 6 months
Questions? email us at orders@meadowlanepantry.com

We have attached a sample of a competitor. The Kibble Crate.

Target Market(s)

Dog owners

Industry/Entity Type

Dog Food

Font styles to use
Sans Serif

Requirements
Must have
• Read project description above
Nice to have
• Our logo color incorporated
Should not have
• I want it simple.

```html
<!DOCTYPE html>
<html lang="en">
<head>
<meta charset="utf-8">
<title>PupKitchen Dog Food Label</title>
<link rel="stylesheet" href="https://fonts.googleapis.com/css2?family=Montserrat:wght@400;500;600&family=Oswald:wght@400;500&display=swap">
<style>
  :root {
    --page: #f1f1ef;
    --label: #ffffff;
    --brand-green: #2f7a3a;
    --beef: #ee5a2c;
    --chicken: #f7a21b;
    --rice: #f8c245;
    --veg: #7cc142;
    --wave-a: #fbb82a;
    --wave-b: #fdd86a;
    --ink: #2b2b2b;
    --band: #111111;
    --accent: #ef5b2b;
  }
  * { box-sizing: border-box; margin: 0; padding: 0; }
  html, body { width: 1200px; height: 1200px; overflow: hidden; }
  body {
    background: var(--page);
    font-family: "Montserrat", sans-serif;
    color: var(--ink);
    position: relative;
  }
  .label {
    position: absolute;
    left: 290px; top: 105px;
    width: 620px; height: 990px;
    background: var(--label);
    border-radius: 34px;
    overflow: hidden;
    box-shadow: 0 6px 24px rgba(0,0,0,0.12);
  }
  .top-wave { position: absolute; left: 0; top: 0; width: 620px; height: 130px; }
  .brand {
    position: absolute; left: 0; right: 0; top: 255px;
    display: flex; align-items: center; justify-content: center; gap: 16px;
  }
  .brand-dot { width: 46px; height: 46px; border-radius: 50%; background: var(--brand-green); }
  .brand-name {
    font-weight: 500; font-size: 50px; color: var(--brand-green); letter-spacing: 1px;
  }
  .ingredients { position: absolute; left: 0; top: 430px; list-style: none; width: 100%; }
  .ingredient { display: flex; align-items: center; height: 52px; margin-bottom: 22px; }
  .pct {
    width: 155px; height: 50px;
    display: flex; align-items: center; justify-content: flex-end; padding-right: 14px;
    font-family: "Oswald", sans-serif; font-size: 42px; color: #fff; line-height: 1;
  }
  .pct--beef { background: var(--beef); }
  .pct--chicken { background: var(--chicken); }
  .pct--rice { background: var(--rice); }
  .pct--veg { background: var(--veg); }
  .name { margin-left: 16px; font-size: 26px; font-weight: 500; }
  .name small {
    display: block; font-family: "Oswald", sans-serif; font-weight: 400;
    font-size: 19px; margin-top: 2px; letter-spacing: -0.2px;
  }
  .storage {
    position: absolute; left: 0; top: 768px; width: 100%; height: 72px;
    background: var(--band); color: #fff; list-style: none;
    padding: 8px 0 0 32px; font-size: 23px; font-weight: 600; line-height: 30px;
  }
  .storage li::before { content: "• "; }
  .contact { position: absolute; left: 0; top: 860px; width: 100%; height: 130px; }
  .contact-lines { position: absolute; left: 0; top: 0; width: 620px; height: 130px; }
  .questions {
    position: absolute; left: 232px; top: 18px; width: 160px; height: 42px;
    background: var(--accent); color: #fff; font-size: 24px; font-weight: 500;
    display: flex; align-items: center; justify-content: center;
  }
  .email-lead { position: absolute; left: 38px; top: 68px; font-size: 16px; }
  .email { position: absolute; left: 38px; top: 90px; font-size: 22px; font-weight: 500; white-space: nowrap; }
  .dog-art {
    position: absolute; left: 462px; top: 22px; width: 112px; height: 96px;
    background: var(--brand-green); border-radius: 10px; opacity: 0.9;
  }
  .base-line { position: absolute; left: 0; bottom: 6px; width: 100%; height: 4px; background: var(--brand-green); }
</style>
</head>
<body>
  <main class="label">
    <svg class="top-wave" viewBox="0 0 620 130" aria-hidden="true">
      <defs>
        <linearGradient id="waveFill" x1="0" y1="0" x2="1" y2="0">
          <stop offset="0" stop-color="var(--wave-a)"/>
          <stop offset="1" stop-color="var(--wave-b)"/>
        </linearGradient>
      </defs>
      <path d="M0 0 H410 C380 20 330 30 260 34 C160 40 80 60 0 125 Z" fill="url(#waveFill)"/>
    </svg>

    <div class="brand">
      <span class="brand-dot"></span>
      <span class="brand-name">PupKitchen</span>
    </div>

    <ul class="ingredients">
      <li class="ingredient"><span class="pct pct--beef">50%</span><span class="name">Choice Beef</span></li>
      <li class="ingredient"><span class="pct pct--chicken">20%</span><span class="name">Pasture-raised Chicken</span></li>
      <li class="ingredient"><span class="pct pct--rice">15%</span><span class="name">Brown Rice</span></li>
      <li class="ingredient"><span class="pct pct--veg">15%</span><span class="name">Fresh Vegetables<small>- Carrots, Kale, Zucchini Herbal Health Boosters</small></span></li>
    </ul>

    <ul class="storage">
      <li>Keeps in fridge for 4 days after thawing.</li>
      <li>Stores in freezer up to 6 months.</li>
    </ul>

    <section class="contact">
      <svg class="contact-lines" viewBox="0 0 620 130" aria-hidden="true">
        <path d="M232 39 H24 V120" fill="none" stroke="var(--accent)" stroke-width="2"/>
        <line x1="392" y1="39" x2="452" y2="39" stroke="var(--accent)" stroke-width="2"/>
      </svg>
      <div class="questions">Questions?</div>
      <p class="email-lead">email us at</p>
      <p class="email">orders@meadowlanepantry.com</p>
      <div class="dog-art" role="img" aria-label="Green silhouette of a standing dog"></div>
    </section>

    <div class="base-line"></div>
  </main>
</body>
</html>
```